Professional Home Buyer business card needed

I need a pretty straight forward business card designed. We help people that NEED to sell their homes solve problems. We perform all types of Real Estate transactions including flip, wholesale, investment, rental property and multi family. The card will mainly be used to give to prospective Sellers but will also be given to Real Estate Investors as well. It should professional and very easy to read, most clients are older people.

Target Market(s)

Distressed home sellers as well as Real Estate investors

Industry/Entity Type

Real Estate

Contact Information for Business Card

should be a professional layout

Colors
ec1f27
ffffff
000000

Requirements
Must have
• Large logo on back and smaller one on front. should utilize Red, white, and black.
• I am thinking of using a soft touch coating on the card so keep that in mind.
• Contact info should be very easy to read, think older clients.
Nice to have
• I would like to see a design with rounded corners on the card
Should not have
• pictures of homes or other home graphics.

```html
<!DOCTYPE html>
<html lang="en">
<head>
<meta charset="utf-8">
<title>Keystone Home Buyers – Business Card</title>
<link href="https://fonts.googleapis.com/css2?family=Lato:wght@400;700&display=swap" rel="stylesheet">
<style>
  :root {
    --red: #ec1f27;
    --white: #ffffff;
    --black: #000000;
    --card-dark: #232324;
    --stage: #161616;
    --ink: #1a1a1a;
  }
  * { box-sizing: border-box; margin: 0; padding: 0; }
  html, body {
    width: 1200px; height: 912px; overflow: hidden;
    background: var(--stage);
    font-family: "Lato", Arial, sans-serif;
  }
  .stage {
    width: 1200px; height: 912px;
    display: flex; flex-direction: column; align-items: center; justify-content: center;
    gap: 40px;
  }
  .card {
    position: relative;
    width: 700px; height: 400px;
    border-radius: 30px;
    overflow: hidden;
  }

  /* Back */
  .card--back { background: var(--card-dark); }
  .back-brand {
    position: absolute; left: 0; right: 0; top: 130px;
    display: flex; align-items: center; justify-content: center; gap: 18px;
  }
  .brand-mark { width: 26px; height: 26px; background: var(--red); flex: none; }
  .back-brand .brand-name {
    color: var(--white); font-weight: 700; font-size: 46px; letter-spacing: 3px;
    line-height: 1.1; text-align: left;
  }
  .back-web {
    position: absolute; left: 0; right: 0; bottom: 56px;
    text-align: center; color: var(--white); font-size: 22px; letter-spacing: .5px;
  }

  /* Front */
  .card--front { background: var(--white); color: var(--ink); }
  .front-brand {
    position: absolute; left: 56px; top: 70px;
    display: flex; align-items: center; gap: 14px;
  }
  .front-brand .brand-mark { width: 20px; height: 20px; }
  .front-brand .brand-name {
    color: var(--black); font-weight: 700; font-size: 28px; letter-spacing: 2px; line-height: 1.15;
  }
  .person { position: absolute; right: 52px; top: 126px; text-align: right; }
  .person__name { color: var(--red); font-size: 32px; font-weight: 700; letter-spacing: -.5px; }
  .person__role { font-size: 18px; margin-top: 2px; }
  .divider {
    position: absolute; left: 56px; right: 52px; top: 208px;
    height: 2px; background: var(--red);
  }
  .address {
    position: absolute; right: 52px; top: 226px; text-align: right;
    font-size: 20px; line-height: 1.3;
  }
  .contacts {
    position: absolute; left: 56px; top: 236px;
    list-style: none; font-size: 22px; line-height: 1.4;
  }
  .contacts li { display: flex; align-items: center; gap: 12px; }
  .contacts svg { width: 18px; height: 18px; fill: var(--red); flex: none; }
  .swoosh { position: absolute; left: 0; top: 0; width: 700px; height: 400px; }
  .front-web {
    position: absolute; right: 30px; bottom: 14px;
    color: var(--white); font-size: 17px; letter-spacing: .3px;
  }
</style>
</head>
<body>
<main class="stage">
  <section class="card card--back">
    <div class="back-brand">
      <span class="brand-mark"></span>
      <span class="brand-name">KEYSTONE<br>HOME BUYERS</span>
    </div>
    <p class="back-web">www.keystonehomebuyers.com</p>
  </section>

  <section class="card card--front">
    <svg class="swoosh" viewBox="0 0 700 400" aria-hidden="true">
      <path class="swoosh__red" d="M260 400 C400 340 560 310 700 300 L700 325 C580 335 450 360 330 400 Z" fill="var(--red)"/>
      <path class="swoosh__black" d="M330 400 C450 360 580 335 700 325 L700 400 Z" fill="var(--black)"/>
    </svg>

    <div class="front-brand">
      <span class="brand-mark"></span>
      <span class="brand-name">KEYSTONE<br>HOME BUYERS</span>
    </div>

    <div class="person">
      <p class="person__name">Daniel Harper</p>
      <p class="person__role">Manager</p>
    </div>

    <div class="divider"></div>

    <p class="address">418 Maple Ridge Lane<br>Brookvale, ST 00412</p>

    <ul class="contacts">
      <li>
        <svg viewBox="0 0 24 24"><path d="M6.6 10.8a15 15 0 0 0 6.6 6.6l2.2-2.2a1 1 0 0 1 1-.25 11.4 11.4 0 0 0 3.6.57 1 1 0 0 1 1 1V20a1 1 0 0 1-1 1A17 17 0 0 1 3 4a1 1 0 0 1 1-1h3.5a1 1 0 0 1 1 1c0 1.25.2 2.45.57 3.57a1 1 0 0 1-.25 1z"/></svg>
        <span>555 201 0140</span>
      </li>
      <li>
        <svg viewBox="0 0 24 24"><path d="M6 2h12v5H6zM4 8h16a2 2 0 0 1 2 2v6h-4v6H6v-6H2v-6a2 2 0 0 1 2-2zm4 8v4h8v-4z"/></svg>
        <span>555 201 0141</span>
      </li>
      <li>
        <svg viewBox="0 0 24 24"><path d="M2 5h20v14H2zm2 2v.5l8 5 8-5V7l-8 5z"/></svg>
        <span>info@keystonehomebuyers.com</span>
      </li>
    </ul>

    <p class="front-web">www.keystonehomebuyers.com</p>
  </section>
</main>
</body>
</html>
```